We are a physical therapy billing company. We need a postcard style flyer.

See attached. We are trying to generate more business for our physical therapy billing company. Our company name is Stridewell Claims Partners.

Industry/Entity Type

Physical Therapy

```html
<!DOCTYPE html>
<html lang="en">
<head>
<meta charset="utf-8">
<title>Stridewell Claims Partners Postcard</title>
<link rel="stylesheet" href="https://fonts.googleapis.com/css2?family=Open+Sans:ital,wght@0,700;0,800;1,800&display=swap">
<style>
:root{
  --frame:#46617f;
  --navy:#1f4e8c;
  --ink:#163a6b;
  --heading:#2c4a6b;
  --panel-light:#f4f6f8;
  --box-line:#5a7896;
  --white:#ffffff;
}
*{margin:0;padding:0;box-sizing:border-box}
html,body{width:767px;height:1200px;overflow:hidden;background:#fff}
body{font-family:"Open Sans",Arial,sans-serif}
.canvas{position:relative;width:767px;height:1200px;background:var(--frame);border-radius:30px;overflow:hidden}
.front,.back{position:absolute;left:38px;width:690px;overflow:hidden}
.front{top:44px;height:532px;background:var(--panel-light)}
.back{top:624px;height:532px;background:linear-gradient(180deg,#f7f8f9,#eef1f4 30%,#fafafa)}

.header-band{position:absolute;left:0;top:0;width:690px;height:148px;
  background:linear-gradient(90deg,#7d93aa 0%,#5a7896 40%,#a9b7c6 70%,#e6eaee 100%)}
.brand-mark{position:absolute;display:flex;align-items:center;gap:8px;font-weight:800;color:var(--navy)}
.header-band .brand-mark{left:30px;top:52px;font-size:34px;color:var(--white)}
.brand-dot{width:18px;height:18px;border-radius:50%;background:#3ad24a}
.headline{position:absolute;left:193px;top:24px;color:var(--white);font-weight:800;font-size:15.5px;line-height:20.5px;
  text-shadow:1px 1px 2px rgba(0,0,0,.6)}
.headline p+p{margin-top:20px}

.photo{position:absolute;left:0;top:148px;width:690px;height:238px;
  background:linear-gradient(90deg,#c9cdd1 0%,#efeae6 30%,#f3ede8 55%,#dfe3e6 80%,#eef1f3 100%)}
.why{position:absolute;left:470px;top:206px;font-size:28px;font-weight:800;color:var(--heading);
  -webkit-text-stroke:1px #fff;text-shadow:2px 2px 3px rgba(0,0,0,.35)}

.lower-band{position:absolute;left:0;top:386px;width:690px;height:146px;
  background:linear-gradient(90deg,#6f88a1,#9fb0c1 50%,#dfe5ea)}
.col-title{position:absolute;top:333px;width:214px;text-align:center;font-size:16px;font-weight:800;color:var(--heading);
  -webkit-text-stroke:.6px #fff;text-shadow:1px 1px 2px rgba(0,0,0,.35)}
.feature{position:absolute;top:358px;width:214px;height:162px;border:1.5px solid var(--box-line);border-radius:40px 40px 4px 4px;
  background:linear-gradient(180deg,rgba(255,255,255,.92),rgba(225,232,238,.88));
  text-align:center;font-size:9.6px;font-weight:700;color:var(--ink);overflow:hidden}
.f1{left:12px;padding:16px 9px 0;line-height:12px}
.f2{left:238px;padding:5px 6px 0;line-height:10.9px}
.f3{left:464px;padding:26px 9px 0;line-height:12px}

.back-top{position:absolute;left:0;top:0;width:690px;height:150px;background:linear-gradient(180deg,#fff,#e6eaee)}
.back .brand-mark{left:92px;top:46px;font-size:42px}
.rule-h{position:absolute;left:0;width:690px;height:5px;background:linear-gradient(90deg,rgba(90,120,150,0),rgba(90,120,150,.55) 20%,rgba(90,120,150,.55) 80%,rgba(90,120,150,0))}
.rule-v{position:absolute;left:344px;top:0;width:6px;height:532px;background:linear-gradient(180deg,rgba(90,120,150,.1),rgba(90,120,150,.45) 30%,rgba(90,120,150,.45) 80%,rgba(90,120,150,.1))}
.stamp{position:absolute;left:580px;top:16px;width:88px;height:108px;border:1.5px solid #8a9db0;border-radius:14px;background:#fff;
  display:flex;align-items:center;justify-content:center;font-style:italic;font-weight:800;font-size:16px;color:var(--navy)}
.address-label{position:absolute;left:362px;top:164px;font-size:16px;font-weight:800;color:var(--navy)}
.contact{position:absolute;left:0;top:496px;width:690px;text-align:center;font-size:16.5px;font-weight:800;color:var(--navy)}
</style>
</head>
<body>
<div class="canvas">
  <section class="front">
    <div class="header-band">
      <div class="brand-mark"><span class="brand-dot"></span>SCP</div>
      <div class="headline">
        <p>Billing Issues?</p>
        <p>Let Stridewell Claims Partners relieve those headaches.<br>We guarantee an increase in your collections<br>and a decrease in your accounts receivable.</p>
      </div>
    </div>
    <div class="photo" role="img" aria-label="Smiling billing specialist wearing a headset in a bright office with colleagues behind"></div>
    <div class="why">Why SCP?</div>
    <div class="lower-band"></div>
    <h2 class="col-title" style="left:12px">KNOWLEDGE</h2>
    <h2 class="col-title" style="left:238px">EXPERIENCE</h2>
    <h2 class="col-title" style="left:464px">ANCILLARY INCOME</h2>
    <div class="feature f1">Our billers are trained exclusively in physical therapy billing and collections. SCP will work with the billing system you choose or are currently using. In addition, with one of our owners being a physical therapist herself, SCP has first-hand knowledge in choosing a PT software program that meets documentation standards and maximizes your collections.</div>
    <div class="feature f2">SCP is a physical therapy billing and consulting company with over 25 years of experience in managing physical therapy practices. We are experts in documentation and coding practices, and our billers are trained in Medicare and private payer guidelines and modifiers. SCP has the skills necessary to increase the efficiency and profitability of your clinic by taking the stress of billing and collections away from your staff, and allowing them to do what they do best – take care of patients!</div>
    <div class="feature f3">SCP can also improve your revenue by showing you how to develop additional services beyond standard physical therapy. We can develop a bracing and custom orthotics program for your clinic that enhances patient care and provides additional sources of revenue in a competitive marketplace.</div>
  </section>

  <section class="back">
    <div class="back-top"></div>
    <div class="brand-mark"><span class="brand-dot"></span>SCP</div>
    <div class="stamp">STAMP</div>
    <div class="rule-h" style="top:148px"></div>
    <div class="rule-h" style="top:474px"></div>
    <div class="rule-v"></div>
    <div class="address-label">Address:</div>
    <div class="contact">Contact SCP today at stridewellclaimspartners.com or call 301-555-0148.</div>
  </section>
</div>
</body>
</html>
```